Création d'un modèle de compte-rendus
Besoins
Cabinet de recrutement et de conseil en Ressources Humaines, nous intervenons depuis plus de 60 ans auprès d’entreprises afin de pourvoir leurs besoins en recrutement.
Nous intervenons sur tout type de postes, du cadre dirigeant à l’ouvrier, avec une majorité de postes à responsabilités.
Dans le cadre de nos recrutements, nous envoyons à l’entreprise cliente un document de synthèse des candidats intéressants que nous rencontrons. Dans ce document, nous présentons son parcours professionnel, ses informations générales (mobilité, préavis, rémunération…), ses principaux traits de personnalité, son potentiel intellectuel ainsi qu’une conclusion présentant les points forts, les axes de progrès et notre avis sur ce candidat.
Nos synthèses actuelles sont sous la forme d’un document WORD de 4 à 6 pages assez classique et nous souhaiterions avoir un document plus dynamique, tout en restant sobre. Les informations clés doivent être rapides à identifier et accessibles à l’œil facilement.
La cible :
Directeurs Généraux, Directeurs des Ressources Humaines, Responsable Recrutement
Tous secteurs d’activité
Groupes internationaux, Entreprises/Industries nationales ou locales, PME/PMI
Couleurs, favoris et autres exigences :
Cf notre logo et site internet : www.travenor-exemple.fr, tons bleus et blancs principalement
Sobriété, Simplicité
Nous sommes ouverts à toute proposition créative de votre part.

```html
<!DOCTYPE html>
<html lang="fr">
<head>
<meta charset="utf-8">
<title>Synthèse candidat – Marc LEFORT</title>
<link rel="stylesheet" href="https://fonts.googleapis.com/css2?family=Carlito:ital,wght@0,400;0,700&display=swap">
<style>
  :root {
    --blue: #1e8fd2;
    --blue-dark: #1679b8;
    --panel: #e8ebee;
    --text: #1c1c1c;
    --white: #ffffff;
  }
  * { box-sizing: border-box; margin: 0; padding: 0; }
  html, body { width: 847px; height: 1200px; overflow: hidden; background: var(--white); }
  body { font-family: "Carlito", "Calibri", Arial, sans-serif; color: var(--text); }
  .sheet { position: relative; width: 847px; height: 1200px; }

  .brand { position: absolute; left: 42px; top: 18px; display: flex; align-items: center; gap: 8px; }
  .brand-mark { width: 16px; height: 16px; border-radius: 50%; background: var(--blue); }
  .brand-name { font-size: 22px; color: var(--blue); line-height: 1; }
  .brand-tagline { position: absolute; left: 42px; top: 47px; font-size: 9px; color: var(--blue); }

  .doc-ref { position: absolute; right: 48px; top: 20px; text-align: right; font-size: 11.5px; font-weight: 700; color: var(--blue); line-height: 18px; }
  .doc-ref .sub { font-weight: 400; }

  .candidate-avatar { position: absolute; left: 92px; top: 92px; width: 56px; height: 56px; border-radius: 50%; background: var(--blue); }
  .candidate-band { position: absolute; left: 155px; top: 92px; width: 612px; }
  .candidate-band .label { height: 28px; background: var(--blue); color: var(--white); font-weight: 700; font-size: 16px; padding: 4px 12px; }
  .candidate-band .name { height: 28px; background: var(--panel); color: var(--blue); font-weight: 700; font-size: 15px; padding: 5px 12px; }

  .section-title { font-size: 16.5px; font-weight: 700; color: var(--blue); text-transform: uppercase; border-bottom: 2px solid var(--blue); padding-bottom: 1px; margin-bottom: 6px; }

  .summary { position: absolute; left: 82px; top: 180px; width: 685px; }
  .summary-grid { background: var(--panel); height: 115px; display: grid; grid-template-columns: 296px 1fr; padding: 10px 10px; row-gap: 0; }
  .trait { display: flex; align-items: center; font-size: 14.5px; font-weight: 700; height: 32px; }
  .rating { display: flex; gap: 2px; width: 98px; }
  .dot { width: 11px; height: 11px; border-radius: 50%; border: 1.5px solid var(--blue); }
  .dot.on { background: var(--blue); }

  .content { position: absolute; left: 82px; top: 352px; width: 685px; }
  .content section { margin-bottom: 14px; }
  .content p { font-size: 15px; line-height: 20px; margin-bottom: 14px; }
  .content section p:last-child { margin-bottom: 0; }

  .footer { position: absolute; left: 42px; right: 48px; top: 1165px; height: 13px; background: var(--blue); color: var(--white); font-size: 9px; font-weight: 700; display: flex; justify-content: space-between; align-items: center; padding: 0 8px; }
</style>
</head>
<body>
<div class="sheet">
  <div class="brand"><span class="brand-mark"></span><span class="brand-name">Travenor Conseil</span></div>
  <div class="brand-tagline">Recrutement &amp; Ressources Humaines</div>

  <div class="doc-ref">
    4329 – Evaluation d’un(e) Directeur(trice) Commercial(e) Export h/f<br>
    <span class="sub">Candidature de Marc LEFORT</span>
  </div>

  <div class="candidate-avatar" role="img" aria-label="Pictogramme du candidat"></div>
  <div class="candidate-band">
    <div class="label">CANDIDAT</div>
    <div class="name">Marc LEFORT</div>
  </div>

  <div class="summary">
    <h2 class="section-title">Resume</h2>
    <div class="summary-grid">
      <div class="trait"><span class="rating"><i class="dot on"></i><i class="dot on"></i><i class="dot"></i><i class="dot"></i><i class="dot"></i></span>Relationnel</div>
      <div class="trait"><span class="rating"><i class="dot on"></i><i class="dot on"></i><i class="dot on"></i><i class="dot on"></i><i class="dot"></i></span>Management</div>
      <div class="trait"><span class="rating"><i class="dot on"></i><i class="dot on"></i><i class="dot on"></i><i class="dot"></i><i class="dot"></i></span>Gestion des émotions</div>
      <div class="trait"><span class="rating"><i class="dot on"></i><i class="dot on"></i><i class="dot on"></i><i class="dot"></i><i class="dot"></i></span>Méthode de travail et autonomie</div>
      <div class="trait"><span class="rating"><i class="dot on"></i><i class="dot on"></i><i class="dot on"></i><i class="dot"></i><i class="dot"></i></span>Commercial</div>
      <div class="trait"><span class="rating"><i class="dot on"></i><i class="dot on"></i><i class="dot on"></i><i class="dot"></i><i class="dot"></i></span>Potentiel intellectuel</div>
    </div>
  </div>

  <div class="content">
    <section>
      <h2 class="section-title">Situation</h2>
      <p>Et prima post Osdroenam quam, ut dictum est, ab hac descriptione discrevimus, Commagena, nunc Euphratensis, clementer adsurgit, Hierapoli, vetere Nino et Samosata civitatibus amplis inlustris.</p>
      <p>Eo adducta re per Isauriam, rege Persarum bellis finitimis inligato repellenteque a conlimitiis suis ferocissimas gentes, quae mente quadam versabili hostiliter eum saepe incessunt et in nos arma moventem aliquotiens iuvant, Nohodares quidam nomine e numero optimatum, incursare Mesopotamiam quotiens copia dederit ordinatus, explorabat nostra sollicite, si repperisset usquam locum vi subita perrupturus.</p>
      <p>Metuentes igitur idem latrones Lycaoniam magna parte campestrem cum se inpares nostris fore congressione stataria documentis frequentibus scirent, tramitibus deviis petivere Pamphyliam diu quidem intactam sed timore populationum et caedium, milite per omnia diffuso propinqua, magnis undique praesidiis conmunitam.</p>
      <p>Tu autem, Fanni, quod mihi tantum tribui dicis quantum ego nec adgnosco nec postulo, facis amice; sed, ut mihi videris, non recte iudicas de Catone; aut enim nemo, quod quidem magis credo, aut si quisquam, ille sapiens fuit. Quo modo, ut alia omittam, mortem filii tulit! memineram Paulum, videram Galum, sed hi in pueris, Cato in perfecto et spectato viro.</p>
      <p>Quibus occurrere bene pertinax miles explicatis ordinibus parans hastisque feriens scuta qui habitus iram pugnantium concitat et dolorem proximos iam gestu terrebat sed eum in certamen alacriter consurgentem revocavere ductores rati intempestivum anceps subire certamen cum haut longe muri distarent, quorum tutela securitas poterat in solido locari cunctorum.</p>
    </section>
    <section>
      <h2 class="section-title">Motivations et ambitions professionnelles</h2>
      <p>Hac ita persuasione reducti intra moenia bellatores obseratis undique portarum aditibus, propugnaculis insistebant et pinnis, congesta undique saxa telaque habentes in promptu, ut si quis se proripuisset interius, multitudine missilium sterneretur et lapidum.</p>
    </section>
    <section>
      <h2 class="section-title">Informations generales</h2>
      <p>Eodem tempore etiam Hymetii praeclarae indolis viri negotium est actitatum, cuius hunc novimus esse textum. cum Africam pro consule regeret Carthaginiensibus victus inopia iam lassatis, ex horreis Romano populo destinatis frumentum dedit, pauloque postea cum provenisset segetum copia, integre sine ulla restituit mora.</p>
    </section>
  </div>

  <div class="footer">
    <span>DOCUMENT CONFIDENTIEL – NE PAS COMMUNIQUER AU CANDIDAT</span>
    <span>28 avril 2017</span>
  </div>
</div>
</body>
</html>
```